Kiosk Coin Venture: Safe and Secure Cash Money

Front of card: LOGO

Back of card:
$$$ FREE ATM PLACEMENT $$$
BENIFITS OF HAVING AN ATM AT YOUR BUSINESS
FREE ATM and BTM (Bitcoin) installation, maintenance, and loading.
Lower card processing fees
Stimulate more traffic.
Ease of access for customers
Maintain customers inside location.
Higher tips and spending

Contact me for more information!
Name: Tomas Redilla
Phone: (555) 318-7742 - Call or Text
Email: Tomas@VaultLinkpay.example

Contact Information for Business Card

The card should be shape of the logo. Only the back will have all the contact and business details.

Requirements
Must have
• The logo itself will be one side, the card will be the shape of the logo. contact details on back side.

```html
<!DOCTYPE html>
<html lang="en">
<head>
<meta charset="utf-8">
<title>VaultLink Pay LLC – Shield Business Card</title>
<link rel="stylesheet" href="https://fonts.googleapis.com/css2?family=Bebas+Neue&display=swap">
<style>
  :root {
    --page-bg: #ececec;
    --card-dark: #1f1f1f;
    --silver-light: #f4f4f4;
    --silver-mid: #bdbdbd;
    --silver-dark: #7a7a7a;
    --ink-light: #ffffff;
    --ink-dark: #1a1a1a;
    --gold: #e2c045;
  }
  * { margin: 0; padding: 0; box-sizing: border-box; }
  html, body {
    width: 1200px;
    height: 900px;
    overflow: hidden;
    background: var(--page-bg);
    font-family: "Bebas Neue", sans-serif;
  }
  .canvas { position: relative; width: 1200px; height: 900px; }

  .card {
    position: absolute;
    width: 424px;
    height: 632px;
  }
  .card--back { left: 128px; top: 126px; }
  .card--front { left: 636px; top: 122px; }
  .card__shape { position: absolute; inset: 0; width: 100%; height: 100%; }

  .line {
    position: absolute;
    left: 0;
    right: 0;
    text-align: center;
    color: var(--ink-light);
    white-space: nowrap;
  }
  .offer-title { top: 97px; font-size: 33px; line-height: 34px; }
  .benefit-band {
    position: absolute;
    left: 8px; right: 8px; top: 150px; height: 40px;
    background: linear-gradient(90deg, var(--silver-dark), var(--silver-light) 30%, var(--silver-mid) 55%, var(--silver-light) 80%, var(--silver-dark));
  }
  .benefit-heading { top: 158px; font-size: 23px; line-height: 24px; color: var(--ink-dark); }
  .service-line { font-size: 21px; line-height: 22px; }
  .service-line--1 { top: 203px; }
  .service-line--2 { top: 231px; }
  .benefit-list { list-style: none; }
  .benefit-item { font-size: 14.5px; line-height: 16px; }
  .benefit-item::before { content: "• "; }
  .benefit-item--1 { top: 272px; }
  .benefit-item--2 { top: 293px; }
  .benefit-item--3 { top: 315px; }
  .benefit-item--4 { top: 336px; }
  .cta { top: 370px; font-size: 29px; line-height: 30px; }
  .contact-name { top: 420px; font-size: 28px; line-height: 29px; }
  .contact-role { top: 455px; font-size: 15px; line-height: 15px; }
  .contact-divider { position: absolute; top: 484px; left: 0; width: 424px; height: 20px; }
  .contact-phone { top: 518px; font-size: 16px; line-height: 17px; }
  .contact-email { top: 539px; font-size: 16px; line-height: 17px; }

  .brand-name {
    position: absolute;
    left: 0; right: 0;
    top: 250px;
    text-align: center;
    font-size: 78px;
    line-height: 76px;
    color: var(--silver-light);
  }
</style>
</head>
<body>
<main class="canvas">

  <section class="card card--back" aria-label="Card back with contact details">
    <svg class="card__shape" viewBox="0 0 530 790" preserveAspectRatio="none" aria-hidden="true">
      <defs>
        <linearGradient id="rim-back" x1="0" y1="0" x2="1" y2="1">
          <stop offset="0" stop-color="#ffffff"/>
          <stop offset="0.45" stop-color="#9a9a9a"/>
          <stop offset="0.7" stop-color="#e8e8e8"/>
          <stop offset="1" stop-color="#6e6e6e"/>
        </linearGradient>
      </defs>
      <path d="M265 0 L530 80 V600 Q530 650 480 680 L265 790 L50 680 Q0 650 0 600 V80 Z" fill="url(#rim-back)"/>
      <path d="M265 12 L518 88 V596 Q518 642 472 670 L265 776 L58 670 Q12 642 12 596 V88 Z" fill="var(--card-dark)"/>
    </svg>
    <h1 class="line offer-title">$$$ Free ATM Placement $$$</h1>
    <div class="benefit-band"></div>
    <h2 class="line benefit-heading">Benifits of having an ATM at your business</h2>
    <p class="line service-line service-line--1">Free ATM and BTM (Bitcoin) installation</p>
    <p class="line service-line service-line--2">maintenance, and loading.</p>
    <ul class="benefit-list">
      <li class="line benefit-item benefit-item--1">Lower card processing fees</li>
      <li class="line benefit-item benefit-item--2">Ease of access for customers</li>
      <li class="line benefit-item benefit-item--3">Maintain customers inside location</li>
      <li class="line benefit-item benefit-item--4">Higher tips and spending</li>
    </ul>
    <p class="line cta">Contact me for more information!</p>
    <p class="line contact-name">Tomas Redilla</p>
    <p class="line contact-role">Owner</p>
    <svg class="contact-divider" viewBox="0 0 424 20" aria-hidden="true">
      <line x1="92" y1="10" x2="180" y2="10" stroke="#ffffff" stroke-width="1"/>
      <line x1="244" y1="10" x2="332" y2="10" stroke="#ffffff" stroke-width="1"/>
      <rect x="187" y="2" width="16" height="16" rx="4" fill="#ffffff"/>
      <path d="M190 10 Q195 5 200 10 L198 12 L196 10.5 L194 10.5 L192 12 Z" fill="var(--card-dark)"/>
      <rect x="191.5" y="11.5" width="7" height="3.5" rx="0.8" fill="var(--card-dark)"/>
      <rect x="221" y="2" width="16" height="16" rx="4" fill="#ffffff"/>
      <rect x="224" y="6" width="10" height="8" fill="var(--card-dark)"/>
      <path d="M224 6 L229 10.5 L234 6" fill="none" stroke="#ffffff" stroke-width="1"/>
    </svg>
    <p class="line contact-phone">(555) 318-7742 - Call or Text</p>
    <p class="line contact-email">Tomas@VaultLinkpay.example</p>
  </section>

  <section class="card card--front" aria-label="Card front with company name">
    <svg class="card__shape" viewBox="0 0 530 790" preserveAspectRatio="none" aria-hidden="true">
      <defs>
        <linearGradient id="rim-front" x1="0" y1="0" x2="1" y2="1">
          <stop offset="0" stop-color="#ffffff"/>
          <stop offset="0.45" stop-color="#9a9a9a"/>
          <stop offset="0.7" stop-color="#e8e8e8"/>
          <stop offset="1" stop-color="#6e6e6e"/>
        </linearGradient>
      </defs>
      <path d="M265 0 L530 80 V600 Q530 650 480 680 L265 790 L50 680 Q0 650 0 600 V80 Z" fill="url(#rim-front)"/>
      <path d="M265 12 L518 88 V596 Q518 642 472 670 L265 776 L58 670 Q12 642 12 596 V88 Z" fill="var(--card-dark)"/>
      <circle cx="265" cy="130" r="62" fill="var(--gold)"/>
    </svg>
    <p class="brand-name">VaultLink<br>Pay LLC</p>
  </section>

</main>
</body>
</html>
```